A combined poster for Martial arts club and Dance club.

We need a poster that will be hung opp and used in street bucks for advertisement. We are two independent clubs ( a dance studio and a MA gym) but have chosen to cooperate and split costs for advertisement. We also see an effect with both arts on the same poster.

We have a attached a picture with both arts doing a pose from each other. This would be great to use.

Target Market(s)

All ages primarily young people

Industry/Entity Type

Martial Art

Colors

Designer to choose colors to be used in the design.

Requirements
Must have
• A professional look. Both logos and either one of the attached pictures.
• Fight styles: Check webpage: http://www.kestrelforge.no
• Dance Styles: http://tramvikdansehus4.com
• Contact information Address and phone
• Space for texts slogans.
Nice to have
• Photoshop the picture with different background or cut them out.

```html
<!DOCTYPE html>
<html lang="no">
<head>
<meta charset="utf-8">
<title>Discover Your Talents – Kestrel Forge & Tramvik Dansehus 4</title>
<link href="https://fonts.googleapis.com/css2?family=Montserrat:wght@500;700;800&display=swap" rel="stylesheet">
<style>
  :root {
    --page-bg: #eceef0;
    --blue: #15a9df;
    --blue-deep: #0c98cf;
    --pink: #e56ca6;
    --pink-deep: #d75993;
    --gi-white: #f4f6f8;
    --gi-shade: #cfd9e2;
    --tutu-blue: #6f8fc4;
    --tutu-light: #f3e6ee;
    --ink: #1b1d2a;
    --white: #ffffff;
  }
  * { box-sizing: border-box; margin: 0; padding: 0; }
  html, body { width: 1200px; height: 960px; overflow: hidden; }
  body {
    background: var(--page-bg);
    font-family: "Montserrat", Arial, sans-serif;
    color: var(--ink);
    position: relative;
  }
  .poster {
    position: absolute;
    left: 300px; top: 30px;
    width: 600px; height: 900px;
    display: flex;
    box-shadow: 0 6px 24px rgba(0,0,0,.18);
  }
  .panel { position: relative; width: 50%; height: 100%; overflow: hidden; }
  .panel--martial { background: linear-gradient(180deg, var(--blue) 0%, var(--blue-deep) 100%); }
  .panel--dance { background: linear-gradient(180deg, var(--pink-deep) 0%, var(--pink) 55%, var(--pink-deep) 100%); }

  .headline {
    position: absolute; left: 36px; top: 42px;
    color: var(--white);
    font-weight: 800; font-size: 36px; line-height: 1.04;
    letter-spacing: 2px; text-transform: uppercase;
  }

  .photo { position: absolute; border-radius: 22px; }
  .photo--fighter {
    left: 22px; top: 160px; width: 200px; height: 270px;
    background: linear-gradient(160deg, var(--gi-white) 0%, var(--gi-shade) 55%, #9fc4dc 100%);
    box-shadow: 0 10px 28px rgba(0,60,100,.22);
  }
  .photo--dancer {
    left: 48px; top: 220px; width: 190px; height: 400px;
    background: linear-gradient(180deg, var(--tutu-light) 0%, var(--tutu-blue) 32%, var(--tutu-light) 52%, #f1c9db 100%);
    box-shadow: 0 10px 28px rgba(120,20,70,.22);
  }

  .brand {
    position: absolute; display: flex; align-items: center; gap: 9px;
    font-weight: 800; letter-spacing: 1px; text-transform: uppercase;
    color: var(--ink); white-space: nowrap;
  }
  .brand__dot { width: 26px; height: 26px; border-radius: 50%; background: var(--ink); flex: none; }
  .panel--martial .brand { left: 26px; top: 640px; font-size: 18px; }
  .panel--dance .brand { left: 28px; top: 643px; font-size: 14px; }

  .styles {
    position: absolute; list-style: none;
    font-size: 9.5px; font-weight: 700; letter-spacing: .8px;
    text-transform: uppercase; line-height: 1.5;
  }
  .styles li::before { content: ". "; }
  .panel--martial .styles { left: 26px; top: 690px; }
  .panel--dance .styles { left: 28px; top: 690px; }

  .contact {
    position: absolute;
    font-size: 8.5px; font-weight: 700; line-height: 1.55;
  }
  .panel--martial .contact { left: 48px; top: 828px; }
  .panel--dance .contact { left: 88px; top: 832px; }
</style>
</head>
<body>
  <main class="poster">
    <section class="panel panel--martial">
      <div class="photo photo--fighter" role="img" aria-label="Photo: martial artist in white gi and black belt leaping in a ballet pose"></div>
      <div class="brand"><span class="brand__dot"></span>Kestrel Forge</div>
      <ul class="styles">
        <li>Brasiliansk Jiu-Jitsu</li>
        <li>Mixed Martial Arts (MMA)</li>
        <li>Thaiboksing (Muay Thai)</li>
        <li>Kyokushin Karate ("Åpen Hånd")</li>
        <li>Submission Wrestling</li>
        <li>Kungfu Tigers Kids (5-7 years)</li>
      </ul>
      <p class="contact">
        Brattlia 12, 1480 Sandvoll - 3 etg<br>
        +47 912 30 458 - +47 933 71 204<br>
        www.kestrelforge.no
      </p>
    </section>

    <section class="panel panel--dance">
      <h1 class="headline">Discover<br>your<br>talents.</h1>
      <div class="photo photo--dancer" role="img" aria-label="Photo: ballerina in blue tutu standing in a fighting stance"></div>
      <div class="brand"><span class="brand__dot"></span>Tramvik Dansehus 4</div>
      <ul class="styles">
        <li>Jazz</li>
        <li>Freestyle</li>
        <li>Disco</li>
        <li>Cheerdance</li>
        <li>Basistrening</li>
        <li>Barn/unge med spesielle behov</li>
        <li>Akrobatikk/turn</li>
        <li>Slowdance</li>
        <li>Barnedans</li>
      </ul>
      <p class="contact">
        Brattlia 12, 1480 Sandvoll<br>
        +47 61 42 85 19<br>
        www.tramvikdansehus4.com
      </p>
    </section>
  </main>
</body>
</html>
```